Benefit Porter

Need home page design for new website. The winner will have the opportunity to design the entire site.

I have attached 3 files.

1) Sort of a site map. PLEASE do not design the home page based on this wire frame. Be creative and use your expertise.

2) Tagline and Copy for the home page. Please just greek in or make up copy for areas that do not have copy at this time.

3) The logo.
Updates

Hi everyone, I am sorry for the delay. I have been out of town on unexpected business. I will make a decision this week. Thank you all for the great designs. Dale

```html
<!DOCTYPE html>
<html lang="en">
<head>
<meta charset="utf-8">
<title>Benefit Porter – Successful, Not Stressful Fundraising</title>
<link rel="stylesheet" href="https://fonts.googleapis.com/css2?family=Source+Sans+3:wght@400;600;700&family=Oswald:wght@500&display=swap">
<style>
  :root {
    --green: #3cb64a;
    --green-bright: #4cd35a;
    --blue: #0d6e94;
    --cream: #fdf8cc;
    --ink: #222;
    --text: #333;
    --muted: #8a8a8a;
    --line: #e2e2e2;
    --footer: #2a2a2a;
    --footer-low: #393939;
    --footer-base: #1f1f1f;
    --white: #fff;
  }
  * { box-sizing: border-box; margin: 0; padding: 0; }
  html, body { width: 980px; height: 1200px; overflow: hidden; }
  body { position: relative; background: var(--white); font-family: Arial, Helvetica, sans-serif; color: var(--text); }
  a { color: var(--blue); text-decoration: underline; }

  .hero { position: absolute; left: 0; top: 0; width: 980px; height: 342px;
    background: linear-gradient(170deg, #8cba4e 0%, #66a030 45%, #45821f 100%); }
  .hero-caption { position: absolute; left: 354px; top: 111px; width: 513px; height: 90px;
    background: rgba(40,40,40,.82); padding: 14px 22px; font-family: "Source Sans 3", sans-serif;
    font-size: 23px; line-height: 28px; color: var(--white); }
  .hero-caption strong { color: var(--green-bright); font-weight: 700; }
  .hero-dots { position: absolute; left: 818px; top: 313px; display: flex; gap: 3px; }
  .hero-dots span { width: 11px; height: 11px; border-radius: 50%; background: var(--white); }
  .hero-dots span:nth-child(2) { background: #a9a9d9; }

  .masthead { position: absolute; left: 0; top: 342px; width: 980px; height: 90px; background: var(--cream); }
  .brand { position: absolute; left: 114px; top: 16px; display: flex; align-items: center; gap: 10px; }
  .brand-mark { width: 52px; height: 52px; border-radius: 50%; background: var(--green); }
  .brand-name { font-family: "Source Sans 3", sans-serif; font-size: 29px; color: var(--green); line-height: 32px; }
  .brand-tag { font-family: "Source Sans 3", sans-serif; font-size: 13.5px; color: var(--ink); margin-top: 1px; }
  .cta { position: absolute; top: 16px; width: 141px; height: 60px; border: 3px solid #d9d9d9; padding: 6px; text-decoration: none; }
  .cta span { display: flex; align-items: center; justify-content: center; height: 100%;
    background: #1e1e1e; color: var(--white); font-family: "Oswald", sans-serif; font-size: 19px; letter-spacing: .3px; }
  .cta-try { left: 576px; background: var(--green); }
  .cta-demo { left: 725px; background: var(--blue); }

  .nav { position: absolute; left: 0; top: 432px; width: 980px; height: 45px; background: var(--blue); }
  .nav ul { list-style: none; display: flex; position: absolute; left: 118px; top: 5px; }
  .nav a { display: block; height: 35px; line-height: 35px; padding: 0 10px; color: var(--white);
    text-decoration: none; font-size: 12px; margin-right: 4px; }
  .nav a.active { background: var(--green); }

  .features { position: absolute; left: 113px; top: 520px; width: 753px; height: 202px;
    display: flex; border-bottom: 2px solid var(--line); }
  .feature { border-left: 1px solid var(--line); position: relative; }
  .feature:last-child { border-right: 1px solid var(--line); }
  .feature h2 { height: 50px; background: var(--green); color: var(--white); font-family: "Source Sans 3", sans-serif;
    font-weight: 400; font-size: 18px; line-height: 50px; padding-left: 11px; border-right: 1px solid #fff;
    white-space: nowrap; overflow: hidden; }
  .feature p { font-size: 11px; line-height: 13px; padding: 9px 11px 0 11px; color: var(--text); }
  .feature a { position: absolute; left: 11px; top: 171px; font-size: 11px; }

  .news { position: absolute; left: 113px; top: 733px; width: 230px; height: 315px; }
  .section-title { font-family: "Source Sans 3", sans-serif; font-weight: 400; font-size: 24px; color: var(--ink); }
  .news .section-title { margin-top: 20px; }
  .news-item { display: flex; gap: 8px; padding: 23px 0 20px; border-bottom: 1px solid var(--line); }
  .news-item + .news-item { border-bottom: none; padding-top: 19px; }
  .news-date { width: 26px; text-align: center; color: var(--blue); }
  .news-date b { display: block; font-size: 19px; line-height: 18px; }
  .news-date small { font-size: 10.5px; }
  .news-item p { font-size: 11px; line-height: 12px; width: 185px; }
  .news .view-all { position: absolute; right: 10px; top: 280px; font-size: 11px; }
  .divider { position: absolute; left: 352px; top: 733px; width: 1px; height: 315px; background: var(--line); }

  .testimonials { position: absolute; left: 367px; top: 733px; width: 500px; height: 315px; }
  .testimonials .section-title { margin-top: 18px; }
  .quote { position: absolute; width: 240px; display: flex; gap: 12px; }
  .quote-photo { width: 84px; height: 74px; border: 2px solid #dcdcdc;
    background: linear-gradient(160deg, #f1d9a8, #e8b99a 55%, #c98d78); flex: none; }
  .quote h3 { font-family: "Source Sans 3", sans-serif; font-weight: 700; font-size: 15px; color: var(--ink); margin: -2px 0 4px; }
  .quote p { font-size: 11px; line-height: 12px; width: 150px; }
  .quote a { font-size: 11px; color: var(--green); }
  .q1 { left: 0; top: 68px; } .q2 { left: 277px; top: 68px; }
  .q3 { left: 0; top: 180px; } .q4 { left: 277px; top: 180px; }
  .testimonials .more { position: absolute; right: 0; top: 297px; font-size: 11px; }

  .rule { position: absolute; left: 113px; top: 1063px; width: 753px; height: 1px; background: var(--line); }

  .footer { position: absolute; left: 0; top: 1100px; width: 980px; height: 100px; background: var(--footer-base); }
  .footer-nav { height: 52px; background: var(--footer); display: flex; justify-content: center; align-items: center;
    list-style: none; font-size: 11px; color: var(--muted); }
  .footer-nav li + li::before { content: "|"; margin: 0 20px; }
  .copyright { height: 36px; line-height: 36px; background: var(--footer-low); text-align: center; font-size: 10px; color: #777; }
</style>
</head>
<body>
  <header class="hero" role="img" aria-label="Close-up photo of a golf ball and putter beside the hole on a green">
    <p class="hero-caption">Charity golf events are <strong>Proven</strong> to be an effective way to <strong>Raise money</strong></p>
    <div class="hero-dots"><span></span><span></span><span></span></div>
  </header>

  <div class="masthead">
    <div class="brand">
      <div class="brand-mark"></div>
      <div>
        <div class="brand-name">BenefitPorter.com</div>
        <div class="brand-tag">Successful, Not Stressful Fundraising</div>
      </div>
    </div>
    <a class="cta cta-try"><span>TRY FOR FREE</span></a>
    <a class="cta cta-demo"><span>DEMO</span></a>
  </div>

  <nav class="nav">
    <ul>
      <li><a class="active">PRICING</a></li>
      <li><a>FEATURES</a></li>
      <li><a>SERVICES</a></li>
      <li><a>PRODUCTS</a></li>
      <li><a>ABOUT</a></li>
      <li><a>CONTACT</a></li>
    </ul>
  </nav>

  <section class="features">
    <article class="feature" style="width:233px">
      <h2>RAISE MORE, STRESS LESS</h2>
      <p>Charity golf events are proven to be an effective way to raise money for worthy causes. But who has the time to manage all the details? You do now, with Benefit Porter.</p>
      <a>Learn More</a>
    </article>
    <article class="feature" style="width:231px">
      <h2>EVERYTHING YOU NEED</h2>
      <p>We are experienced in both the art of fundraising as well as the dynamics of a golf event and we are here to help you. We offer everything from simple self-service tools that include professionally-designed website and email templates all the way up to full service event planning.</p>
      <a>Learn More</a>
    </article>
    <article class="feature" style="width:289px">
      <h2>SOLD! SILENT AUCTION MODUCLE</h2>
      <p>Exclusive to BenefitPorter.com is our Silent Auction module. Through our partners we can add even more value to your golf event. Auction off premium items during the tournament and add to your fundraising!</p>
      <a>Learn More</a>
    </article>
  </section>

  <section class="news">
    <h2 class="section-title">NEWS &amp; EVENTS</h2>
    <div class="news-item">
      <div class="news-date"><b>25</b><small>sept.</small></div>
      <p>Praesent vestibulum aenean nonummy hendrerit mauris. Hasellus porta. Fusce suscipit varius mi. aenean nonummy hendrerit mauris. Hasellus porta. Fusce suscipit varius mi.</p>
    </div>
    <div class="news-item">
      <div class="news-date"><b>20</b><small>sept.</small></div>
      <p>Praesent vestibulum aenean nonummy hendrerit mauris. Hasellus porta. Fusce suscipit varius mi. aenean nonummy hendrerit mauris. Hasellus porta. Fusce suscipit varius mi.</p>
    </div>
    <a class="view-all">View all</a>
  </section>
  <div class="divider"></div>

  <section class="testimonials">
    <h2 class="section-title">TESTIMONIALS</h2>
    <div class="quote q1"><div class="quote-photo" role="img" aria-label="Portrait photo of the client"></div>
      <div><h3>Nora Bell</h3><p>Dasenim ad minim vcipses labosam noase quid eytase eresa ea onsequatursuis autem vel.</p><a>Learn more</a></div></div>
    <div class="quote q2"><div class="quote-photo" role="img" aria-label="Portrait photo of the client"></div>
      <div><h3>Ivy Hale</h3><p>Dasenim ad minim vcipses labosam noase quid eytase eresa ea onsequatursuis autem vel.</p><a>Learn more</a></div></div>
    <div class="quote q3"><div class="quote-photo" role="img" aria-label="Portrait photo of the client"></div>
      <div><h3>Nora Bell</h3><p>Dasenim ad minim vcipses labosam noase quid eytase eresa ea onsequatursuis autem vel.</p><a>Learn more</a></div></div>
    <div class="quote q4"><div class="quote-photo" role="img" aria-label="Portrait photo of the client"></div>
      <div><h3>Ivy Hale</h3><p>Dasenim ad minim vcipses labosam noase quid eytase eresa ea onsequatursuis autem vel.</p><a>Learn more</a></div></div>
    <a class="more">More Testimonials</a>
  </section>

  <div class="rule"></div>

  <footer class="footer">
    <ul class="footer-nav">
      <li>Pricing</li><li>Features</li><li>Services</li><li>Products</li><li>About</li><li>Contact</li>
    </ul>
    <p class="copyright">Copyright 2014 www.benefitporter.com All Rights Reserved.</p>
  </footer>
</body>
</html>
```